Tarn Studio PPT design

We are looking for a fresh and funky PPT design that is both eye-catching and allows room/whitespace for us to get the content across. We are a social media agency based in China and our logo although simple sort of reflects the nature of the company. There are two main tasks for this PPT, one as a business card to show-case our case-studies, but also as a back-drop to our pitch presentations and other client presentations. These presentations are a mix of visuals, text and graphs. The key message we want to get across is that we are professional, creative and fresh. We think that using our four support colours may work but are open to suggestions.
Current website www.tarnasia-example.com
Reason: Hi All,
as we have just guaranteed the payment we extended the deadline to allow for more submissions. Please bear with us.
Thanks,
Tarn Studio Team
Reason: To see more designs, we extend the deadline to March 18, 2014. Thanks.
Target Market(s)
Marketing CMO's, company CEO's, product managers, social media managers
Industry/Entity Type
Business

```html
<!DOCTYPE html>
<html lang="en">
<head>
<meta charset="utf-8">
<title>Tarn Studio – Presentation Template</title>
<link href="https://fonts.googleapis.com/css2?family=Open+Sans:wght@300;400;600;700&display=swap" rel="stylesheet">
<style>
  :root{
    --canvas:#a5adb1;
    --ink:#33323f;
    --paper:#f9f9f9;
    --white:#ffffff;
    --pink:#d9048e;
    --orange:#e05a35;
    --purple:#6b2f8f;
    --green:#8dc63f;
    --accent-orange:#f26522;
    --placeholder:#e6e6e6;
    --placeholder-mark:#d6d6d6;
    --muted:#555560;
  }
  *{box-sizing:border-box;margin:0;padding:0}
  html,body{width:1064px;height:1200px;overflow:hidden}
  body{background:var(--canvas);font-family:"Open Sans",Arial,sans-serif;position:relative}
  .slide{position:absolute;width:516px;overflow:hidden}
  .col-left{left:12px}
  .col-right{left:536px}
  .row-1{top:9px;height:387px}
  .row-2{top:407px;height:386px}
  .row-3{top:804px;height:387px}

  .slide--light{background:var(--paper)}
  .slide--dark{background:radial-gradient(ellipse at 50% 45%,#3a3947 0%,var(--ink) 70%)}
  .slide--pink{background:radial-gradient(ellipse at 50% 45%,#e0109a 0%,var(--pink) 70%)}
  .slide--orange{background:radial-gradient(ellipse at 50% 45%,#e7683f 0%,var(--orange) 70%)}
  .slide--content{background:var(--white)}

  .brand-stripe{position:absolute;left:0;right:0;bottom:0;height:3px;display:flex}
  .brand-stripe span{flex:1}
  .brand-stripe .s1{background:var(--green)}
  .brand-stripe .s2{background:var(--purple)}
  .brand-stripe .s3{background:var(--pink)}
  .brand-stripe .s4{background:var(--accent-orange)}

  /* wordmark */
  .wordmark{position:absolute;display:flex;align-items:center;gap:10px;font-weight:700;letter-spacing:-1px;white-space:nowrap}
  .wordmark .mark-square{display:block;background:var(--accent-orange)}
  .wordmark--hero{left:0;right:0;top:150px;justify-content:center;font-size:60px;color:var(--ink)}
  .wordmark--hero .mark-square{width:16px;height:16px}
  .wordmark--cover{right:262px;top:172px;font-size:34px;line-height:1;color:var(--white)}

  .divider{position:absolute;left:272px;top:160px;width:1px;height:80px;background:rgba(255,255,255,.6)}
  .cover-text{position:absolute;left:281px;top:160px;color:var(--white);font-weight:300;line-height:1.2}
  .cover-title{font-size:19px}
  .cover-sub{font-size:15.5px}
  .cover-date{font-size:12.5px;color:var(--accent-orange)}

  /* content slides */
  .slide-header{position:absolute;left:0;right:0;top:0;height:48px;border-bottom:1px solid #e8e8e8;text-align:center;background:var(--white)}
  .slide-title{font-weight:300;font-size:23px;color:var(--purple);line-height:1;padding-top:6px;letter-spacing:-.2px}
  .slide-kicker{font-size:8.5px;color:var(--muted);margin-top:3px;letter-spacing:.2px}
  .slide-kicker strong{font-weight:700}

  .image-slot{position:absolute;background:var(--placeholder);display:flex;align-items:center;justify-content:center;box-shadow:0 3px 4px rgba(0,0,0,.08)}
  .image-slot--landscape{left:35px;top:69px;width:447px;height:200px}
  .image-slot--portrait{left:267px;top:65px;width:218px;height:275px}

  .feature-list{position:absolute;left:36px;top:281px;width:450px;list-style:none}
  .feature{display:flex;gap:9px;align-items:flex-start;margin-bottom:13px;font-size:7px;line-height:1.35;color:#222}
  .feature svg{flex:none;margin-top:1px}
  .feature strong{font-weight:700}

  .slide-footer{position:absolute;left:0;right:0;bottom:0;height:32px;background:var(--ink);display:flex;align-items:center;padding-left:10px}
  .footer-brand{font-weight:700;font-size:11px;color:var(--white);letter-spacing:-.3px;white-space:nowrap;width:68px;flex:none}
  .footer-label{font-size:8.5px;color:var(--white);letter-spacing:.2px;white-space:nowrap}
  .footer-label strong{font-weight:700}
  .footer-label .to{color:var(--pink)}
  .footer-label .client{color:var(--pink);font-weight:700}
  .footer-label .slash{color:var(--pink);font-weight:400}
  .page-num{position:absolute;right:13px;bottom:6px;font-size:7px;color:var(--pink)}

  .lead{position:absolute;left:33px;top:93px;width:172px;font-size:12px;color:var(--purple);line-height:1.45;letter-spacing:-.3px}
  .lead-arrow{position:absolute;left:210px;top:100px}
  .body-copy{position:absolute;left:33px;top:141px;width:205px;font-size:8.5px;color:var(--muted);line-height:1.45;text-align:justify}
  .body-copy strong{color:var(--ink);font-weight:700}
  .icon-note{position:absolute;left:33px;top:240px;width:205px;font-size:8.5px;color:var(--muted);line-height:1.45;text-align:justify}
  .icon-row{position:absolute;left:34px;display:flex;gap:6px}
  .icon-row--a{top:270px}
  .icon-row--b{top:296px}
  .icon-row svg{display:block;fill:var(--pink)}
</style>
</head>
<body>

<!-- Brand intro -->
<section class="slide slide--light col-left row-1">
  <div class="wordmark wordmark--hero"><span>Tarn Studio</span><span class="mark-square"></span></div>
  <div class="brand-stripe"><span class="s1"></span><span class="s2"></span><span class="s3"></span><span class="s4"></span></div>
</section>

<!-- Cover -->
<section class="slide slide--dark col-right row-1">
  <div class="wordmark wordmark--cover"><span>Tarn Studio</span></div>
  <div class="divider"></div>
  <div class="cover-text">
    <p class="cover-title">PRESENTATION TITLE</p>
    <p class="cover-sub">Presentation Subtitle</p>
    <p class="cover-date">MARCH 2014</p>
  </div>
  <div class="brand-stripe"><span class="s1"></span><span class="s2"></span><span class="s3"></span><span class="s4"></span></div>
</section>

<!-- Landscape image layout -->
<section class="slide slide--content col-left row-2">
  <header class="slide-header">
    <h2 class="slide-title">IMAGE IN LANDSCAPE VIEW</h2>
    <p class="slide-kicker">WITH COMPLETELY <strong>CUSTOMIZABLE</strong> ICONS</p>
  </header>
  <div class="image-slot image-slot--landscape" role="img" aria-label="Landscape image placeholder">
    <svg width="96" height="96" viewBox="0 0 96 96" aria-hidden="true">
      <rect x="4" y="4" width="88" height="88" fill="none" stroke="var(--placeholder-mark)" stroke-width="6"/>
      <circle cx="28" cy="30" r="9" fill="var(--placeholder-mark)"/>
      <polygon points="12,78 34,48 46,62 62,36 84,78" fill="var(--placeholder-mark)"/>
    </svg>
  </div>
  <ul class="feature-list">
    <li class="feature">
      <svg width="18" height="14" viewBox="0 0 18 14" aria-hidden="true"><rect x="1" y="1" width="16" height="9" fill="none" stroke="var(--pink)" stroke-width="2"/><rect x="7" y="10" width="4" height="2" fill="var(--pink)"/><rect x="4" y="12" width="10" height="2" fill="var(--pink)"/></svg>
      <p><strong>Aenean</strong> ridiculus tortor quis interdum id habitant ad, natoque consectetuer nisl auctor libero quisque euismod ante inceptos malesuada ligula mattis.</p>
    </li>
    <li class="feature">
      <svg width="18" height="14" viewBox="0 0 18 14" aria-hidden="true"><polygon points="1,5 5,5 15,1 15,13 5,9 1,9" fill="var(--pink)"/><rect x="5" y="9" width="3" height="5" fill="var(--pink)"/></svg>
      <p><strong>Aenean</strong> ridiculus tortor quis interdum id habitant ad, natoque consectetuer nisl auctor libero quisque euismod ante inceptos malesuada ligula mattis.</p>
    </li>
  </ul>
  <footer class="slide-footer">
    <span class="footer-brand">Tarn Studio</span>
    <span class="footer-label"><strong>COMPANY</strong> PRESENTATION <span class="to">to</span> <span class="client">Business</span><span class="slash">/client</span></span>
    <span class="page-num">3</span>
  </footer>
</section>

<!-- Chapter (pink) -->
<section class="slide slide--pink col-right row-2">
  <div class="wordmark wordmark--cover"><span>Tarn Studio</span></div>
  <div class="divider"></div>
  <div class="cover-text">
    <p class="cover-title">NEW CHAPTER HEADING</p>
    <p class="cover-sub">New Chapter Subtitle</p>
  </div>
</section>

<!-- Portrait image layout -->
<section class="slide slide--content col-left row-3">
  <header class="slide-header">
    <h2 class="slide-title">IMAGE IN PORTRAIT VIEW</h2>
    <p class="slide-kicker">WITH AN EXAMPLE OF DIFFERENT TYPOGRAPHY</p>
  </header>
  <p class="lead">Drag &amp; Drop images here It’s an Image Placeholder</p>
  <svg class="lead-arrow" width="24" height="24" viewBox="0 0 24 24" aria-hidden="true"><circle cx="12" cy="12" r="10.5" fill="none" stroke="var(--ink)" stroke-width="1.2"/><path d="M6 12h11M13 8l4 4-4 4" fill="none" stroke="var(--ink)" stroke-width="1.2"/></svg>
  <p class="body-copy"><strong>Lorem</strong> ipsum dolor sit amet, consectetur adipiscing elit. Vivamus eget elit eu velit vehicula feugiat. Integer viverra metus vitae lectus dictum eleifend. Lorem ipsum dolor sit amet. Donec viverra lobortis feugiat. Sed id odio ante.</p>
  <p class="icon-note">These are a few icon examples you can use, through out the template.</p>
  <div class="icon-row icon-row--a" aria-hidden="true">
    <svg width="11" height="11" viewBox="0 0 12 12"><circle cx="6" cy="6" r="4.5"/><circle cx="6" cy="6" r="1.6" fill="#fff"/></svg>
    <svg width="11" height="11" viewBox="0 0 12 12"><path d="M5 0h2v5h3L6 9 2 5h3z"/><rect x="0" y="10" width="12" height="2"/></svg>
    <svg width="11" height="11" viewBox="0 0 12 12"><rect x="1" y="5" width="10" height="7"/><path d="M3 5V3a3 3 0 0 1 6 0v2" fill="none" stroke="var(--pink)" stroke-width="1.5"/></svg>
    <svg width="11" height="11" viewBox="0 0 12 12"><rect x="3" y="0" width="6" height="2"/><path d="M4 2h4l1 5H3z"/><rect x="5.3" y="7" width="1.4" height="5"/></svg>
    <svg width="11" height="11" viewBox="0 0 12 12"><path d="M0 5h6V2l4 4-4 4V7H0z"/></svg>
    <svg width="11" height="11" viewBox="0 0 12 12"><circle cx="6" cy="6" r="6"/><path d="M4 3l4 3-4 3z" fill="#fff"/></svg>
    <svg width="11" height="11" viewBox="0 0 12 12"><circle cx="6" cy="6" r="5.5"/><path d="M1 6h10M6 1v10" stroke="#fff" stroke-width=".8"/></svg>
    <svg width="13" height="11" viewBox="0 0 14 12"><circle cx="5" cy="7" r="4"/><circle cx="9" cy="6" r="4"/><rect x="2" y="7" width="11" height="4"/></svg>
    <svg width="11" height="11" viewBox="0 0 12 12"><rect x="0" y="3" width="7" height="9" fill="none" stroke="var(--pink)" stroke-width="1.3"/><rect x="4" y="0" width="7" height="9" fill="none" stroke="var(--pink)" stroke-width="1.3"/></svg>
    <svg width="12" height="11" viewBox="0 0 12 12"><rect x="4" y="0" width="4" height="3"/><rect x="0" y="8" width="3" height="3"/><rect x="4.5" y="8" width="3" height="3"/><rect x="9" y="8" width="3" height="3"/><path d="M6 3v3M1.5 8V6h9v2" fill="none" stroke="var(--pink)"/></svg>
    <svg width="13" height="11" viewBox="0 0 14 12"><circle cx="5" cy="6" r="4"/><circle cx="9" cy="5" r="4"/><rect x="2" y="6" width="11" height="4"/><path d="M7 4v5M5 7l2 2 2-2" stroke="#fff" fill="none"/></svg>
  </div>
  <div class="icon-row icon-row--b" aria-hidden="true">
    <svg width="13" height="11" viewBox="0 0 14 12"><rect x="1" y="1" width="12" height="7" fill="none" stroke="var(--pink)" stroke-width="1.5"/><rect x="5" y="9" width="4" height="2"/></svg>
    <svg width="13" height="11" viewBox="0 0 14 12"><rect x="2" y="2" width="10" height="6" fill="none" stroke="var(--pink)" stroke-width="1.3"/><rect x="0" y="9" width="14" height="2"/></svg>
    <svg width="9" height="11" viewBox="0 0 9 12"><rect x="1" y="1" width="7" height="10" rx="1" fill="none" stroke="var(--pink)" stroke-width="1.3"/></svg>
    <svg width="11" height="11" viewBox="0 0 12 12"><rect x="0" y="4" width="8" height="8"/><circle cx="4" cy="3" r="2"/><circle cx="9" cy="8" r="2"/></svg>
    <svg width="12" height="11" viewBox="0 0 12 12"><path d="M2 2h8l2 5v4H0V7z" fill="none" stroke="var(--pink)" stroke-width="1.3"/><path d="M0 7h12"/></svg>
    <svg width="9" height="11" viewBox="0 0 9 12"><circle cx="4.5" cy="4.5" r="3.6" fill="none" stroke="var(--pink)" stroke-width="1.3"/><rect x="3" y="9" width="3" height="3"/></svg>
    <svg width="12" height="11" viewBox="0 0 12 12"><rect x="0" y="0" width="12" height="3"/><rect x="1" y="4" width="10" height="8"/><rect x="4" y="6" width="4" height="1.4" fill="#fff"/></svg>
    <svg width="11" height="11" viewBox="0 0 12 12"><rect x="0" y="1" width="5.5" height="4.8"/><rect x="6.5" y="0" width="5.5" height="5.8"/><rect x="0" y="6.5" width="5.5" height="4.8"/><rect x="6.5" y="6.5" width="5.5" height="5.5"/></svg>
    <svg width="12" height="11" viewBox="0 0 12 12"><rect x="0.6" y="0.6" width="10.8" height="10.8" fill="none" stroke="var(--pink)" stroke-width="1.2"/><rect x="3" y="6" width="1.5" height="4"/><rect x="5.5" y="4" width="1.5" height="6"/><rect x="8" y="3" width="1.5" height="7"/></svg>
  </div>
  <div class="image-slot image-slot--portrait" role="img" aria-label="Portrait image placeholder">
    <svg width="84" height="84" viewBox="0 0 96 96" aria-hidden="true">
      <rect x="4" y="4" width="88" height="88" fill="none" stroke="var(--placeholder-mark)" stroke-width="6"/>
      <circle cx="28" cy="30" r="9" fill="var(--placeholder-mark)"/>
      <polygon points="12,78 34,48 46,62 62,36 84,78" fill="var(--placeholder-mark)"/>
    </svg>
  </div>
  <footer class="slide-footer">
    <span class="footer-brand">Tarn Studio</span>
    <span class="footer-label"><strong>COMPANY</strong> PRESENTATION <span class="to">to</span> <span class="client">Business</span><span class="slash">/client</span></span>
    <span class="page-num">5</span>
  </footer>
</section>

<!-- Chapter (orange) -->
<section class="slide slide--orange col-right row-3">
  <div class="wordmark wordmark--cover"><span>Tarn Studio</span></div>
  <div class="divider"></div>
  <div class="cover-text">
    <p class="cover-title">NEW CHAPTER HEADING</p>
    <p class="cover-sub">New Chapter Subtitle</p>
  </div>
</section>

</body>
</html>
```